"End of year wishes" - Electronic card

Velmora is a regulatory consulting company in the cosmetic sector. We provide premium services and have 12 years of experience.
Please visit our website for more information: https://velmora-example.com
Like every year, we would like to send an electronic design to our clients and partners to wish them happy holidays. This year, we would like to share two good news with them: offer them a surprise (to be revealed later on) and invite them to visit our new brand new website. We relay on your talent and imagination for the design! We need something very professional, serious, beautiful and in line with our graphic layout (see our company website)

Target Market(s)

cosmetic brands

Industry/Entity Type

Cosmetics

Requirements
Must have
• The following statement should be included to the design:

We wish you a Happy Holiday and a Marvelous New Year 2021!
As December is the month of giving, we have a surprise for you. Please contact your dedicated Account Manager to find out more!

Good news never comes alone, we've also updated our website in order to serve you better. We hope you like it as much as we do.
Please enjoy the experience: www.velmora-example.com

```html
<!DOCTYPE html>
<html lang="en">
<head>
<meta charset="utf-8">
<title>Velmora – End of Year Wishes</title>
<link rel="stylesheet" href="https://fonts.googleapis.com/css2?family=Kaushan+Script&family=Montserrat:wght@500;600;700&display=swap">
<style>
  :root {
    --ink: #0b0a0a;
    --green: #8cc63f;
    --green-band: #8fc21f;
    --white: #ffffff;
    --button-text: #33394a;
    --glow: rgba(226, 214, 190, 0.55);
    --tree-red: #b3120e;
    --tree-green: #1f5a3a;
    --tree-gold: #b89a52;
  }
  * { margin: 0; padding: 0; box-sizing: border-box; }
  html, body {
    width: 1200px; height: 1200px; overflow: hidden; background: var(--ink);
  }
  .card {
    position: relative; width: 1200px; height: 1200px; overflow: hidden;
    background:
      radial-gradient(circle at 863px 320px, var(--glow) 0, rgba(160,130,100,0.25) 90px, rgba(60,40,30,0.15) 260px, transparent 480px),
      var(--ink);
    font-family: "Montserrat", sans-serif;
    color: var(--white);
  }
  .tree-photo {
    position: absolute; left: 700px; top: 0; width: 500px; height: 1200px;
    background:
      radial-gradient(circle at 420px 180px, var(--tree-red) 0, rgba(179,18,14,0.7) 70px, transparent 110px),
      radial-gradient(circle at 330px 520px, var(--tree-gold) 0, rgba(184,154,82,0.5) 50px, transparent 80px),
      radial-gradient(circle at 320px 780px, var(--tree-red) 0, rgba(179,18,14,0.6) 60px, transparent 100px),
      radial-gradient(circle at 200px 1000px, var(--tree-red) 0, rgba(179,18,14,0.5) 60px, transparent 110px),
      radial-gradient(ellipse at 360px 700px, var(--tree-green) 0, rgba(31,90,58,0.6) 200px, transparent 330px),
      linear-gradient(90deg, transparent 0, rgba(40,20,15,0.4) 40%, rgba(70,20,15,0.6) 100%);
  }
  .brand {
    position: absolute; left: 942px; top: 20px;
    font-weight: 700; font-size: 34px; letter-spacing: 0.5px; color: var(--white);
  }
  .greeting-intro {
    position: absolute; left: 282px; top: 216px;
    font-weight: 600; font-size: 25px; letter-spacing: 5px; color: var(--white); z-index: 2;
  }
  .greeting-script {
    position: absolute; font-family: "Kaushan Script", cursive; color: var(--green);
    line-height: 1; white-space: nowrap;
  }
  .greeting-script--happy { left: 135px; top: 178px; font-size: 206px; }
  .greeting-script--holiday { left: 62px; top: 405px; font-size: 212px; letter-spacing: 10px; }
  .rule {
    position: absolute; left: 73px; width: 682px; height: 3px; background: var(--green);
  }
  .rule--top { top: 655px; }
  .rule--bottom { top: 729px; }
  .new-year {
    position: absolute; left: 67px; width: 690px; top: 676px; text-align: center;
    font-weight: 700; font-size: 35px; letter-spacing: 0; color: var(--green); white-space: nowrap;
  }
  .message {
    position: absolute; left: 80px; width: 665px; text-align: center;
    font-weight: 600; font-size: 19.5px; line-height: 24.5px; letter-spacing: 1.6px; text-transform: uppercase;
  }
  .message span { display: block; white-space: nowrap; }
  .message--surprise { top: 766px; }
  .message--website { top: 873px; }
  .cta {
    position: absolute; left: 99px; top: 959px; width: 636px; height: 45px;
    background: var(--green-band); color: var(--button-text);
    display: flex; align-items: center; justify-content: center;
    font-weight: 600; font-size: 15.5px; letter-spacing: 0.8px; text-transform: uppercase;
    white-space: nowrap;
  }
</style>
</head>
<body>
<main class="card">
  <div class="tree-photo" role="img" aria-label="Photo of a decorated Christmas tree with red and gold baubles, tinsel, ribbon and a small wrapped gift"></div>

  <div class="brand">velmora</div>

  <p class="greeting-intro">WE WISH YOU A</p>
  <h1>
    <span class="greeting-script greeting-script--happy">Happy</span>
    <span class="greeting-script greeting-script--holiday">Holiday</span>
  </h1>

  <div class="rule rule--top"></div>
  <p class="new-year">AND A MARVELOUS NEW YEAR 2021!</p>
  <div class="rule rule--bottom"></div>

  <p class="message message--surprise">
    <span>As December is the month of giving, we have a sur-</span>
    <span>prise for you. Please contact your dedicated ac-</span>
    <span>count manager to find out more!</span>
  </p>

  <p class="message message--website">
    <span>Good news never comes alone, we've also updated</span>
    <span>our website in order to serve you better. We hope</span>
    <span>you like it as much as we do.</span>
  </p>

  <p class="cta">Please enjoy the experience:&nbsp;www.velmora-example.com</p>
</main>
</body>
</html>
```